Web Design Project for Web Agency

WHAT I NEED:
The design I need (PSD file) is for a microsite designed for employee recruitment for Brantley, a Web agency.
***Design for the 1st Page ONLY : "Manifeste"
OBJECTIVES OF THE WEBSITE:
1. To promote the agency's corporate culture and HR management principles.
2. To get people to apply on available jobs
ELEMENTS OF THE PAGE "MANIFESTE" :
1. Brantley logo (see attached files). Beside the logo must be the word "Carrières" ("Careers" in english)
***The logo is not final and there is NO branding for Brantley yet. That is why there are multiple files. So please feel free to be creative!
2. Main menu : 4 sections
Manifeste | Opportunités | Brantly | Postuler
3. Manifeste :
This page is the home page. It will present 2 main sections :
a. The agency's corporate culture :
- Title of the page is a question : "Do you embrace Brantley's corporate culture?"
- Then, presentation of the 5 corporate values, each with a title and short description
- At the end of the list of values, we want a button that says "Apply now"
b. The agency's HR management principles :
- Title of the page is a question : "Do you see yourself working at Brantley?"
- Then, presentation of the 5 Management principles, each with a title and short description
- At the end of the list of principles, we want a button that says "Apply now"
VISUAL INSPIRATION
To create each section of the "Manifeste" page, we want a design that will fit with the corporate culture:
- Brantley is BOLD
- Brantley is PROUD
- Brantley is PROFESSIONAL
- Brantley is ELEGANT
- Brantley is REFINED
We want something slick and modern. Here are some Website's that we like that can be of inspiration:
- http://www.studio-vetrak.com/en/services
- http://quorvinpanels.com/

```html
<!DOCTYPE html>
<html lang="fr">
<head>
<meta charset="utf-8">
<title>Brantley Carrières — Manifeste</title>
<link rel="stylesheet" href="https://fonts.googleapis.com/css2?family=Ubuntu:wght@400;500;700&family=Open+Sans:ital,wght@0,400;0,600;0,700;1,400&display=swap">
<style>
:root{
  --orange:#f47a35;
  --orange-deep:#e2561a;
  --orange-band:#fa8f2c;
  --orange-band-light:#ffa347;
  --ink:#2b2b2b;
  --body:#5a5a5a;
  --rule:#e6e6e6;
  --footer:#3b3b3b;
  --gold:#f5b700;
  --white:#ffffff;
  --tweet-link:#6fd2ea;
}
*{margin:0;padding:0;box-sizing:border-box}
html,body{width:1200px;height:2250px;overflow:hidden;background:var(--white)}
body{position:relative;font-family:"Open Sans",Arial,sans-serif;color:var(--ink)}

/* Header */
.site-header{position:absolute;left:0;top:0;width:1200px;height:90px;background:var(--white);z-index:2}
.brand{position:absolute;left:168px;top:22px;display:flex;align-items:center;gap:12px}
.brand-mark{width:30px;height:30px;background:var(--orange)}
.brand-name{font-family:"Ubuntu",sans-serif;font-weight:500;font-size:36px;line-height:44px;color:var(--ink)}
.main-nav{position:absolute;left:493px;top:0;display:flex;height:88px}
.main-nav a{display:flex;align-items:center;justify-content:center;height:88px;font-size:15px;color:#222;text-decoration:none;border-right:1px solid #eee}
.main-nav a.is-active{background:var(--orange);color:var(--white)}
.social{position:absolute;left:925px;top:27px;display:flex;gap:8px}
.social span{width:26px;height:26px;border-radius:50%;background:#9a9a9a}

/* Hero */
.hero{position:absolute;left:0;top:90px;width:1200px;height:672px;background:
  radial-gradient(ellipse 520px 300px at 720px 520px,#d9d7d8 0%,rgba(217,215,216,0) 70%),
  linear-gradient(180deg,#c3ccd3 0%,#dcdde0 40%,#a9b1ba 78%,#8e97a3 100%)}
.hero-copy{position:absolute;left:138px;top:198px;width:380px;color:var(--white)}
.hero-title{font-family:"Ubuntu",sans-serif;font-weight:700;font-size:18.5px;line-height:26px;color:var(--orange-deep);white-space:nowrap;text-shadow:0 1px 1px rgba(255,255,255,.6)}
.hero-text{width:370px;font-size:12.5px;line-height:21px;margin-top:16px;text-shadow:0 1px 2px rgba(0,0,0,.45)}
.btn-more{position:absolute;left:226px;top:137px;width:136px;height:37px;border-radius:7px;background:linear-gradient(#ffa54c,#f47a1f);color:var(--white);font-family:"Ubuntu",sans-serif;font-size:18px;display:flex;align-items:center;justify-content:center}
.hero-arrow{position:absolute;top:217px;width:44px;height:44px;border-radius:50%;background:#f1f1f1;border:2px solid #ccc;box-shadow:0 1px 3px rgba(0,0,0,.3)}
.hero-arrow svg{display:block;margin:12px auto}

/* Sections */
.section-rule{position:absolute;left:135px;width:885px;height:1px;background:var(--rule)}
.ribbon{position:absolute;left:360px;width:410px;height:40px;background:var(--orange-deep);clip-path:polygon(0 50%,4% 0,96% 0,100% 50%,96% 100%,4% 100%)}
.ribbon span{position:absolute;left:30px;right:30px;top:0;bottom:0;background:var(--orange);border-radius:20px;display:flex;align-items:center;justify-content:center;color:var(--white);font-family:"Ubuntu",sans-serif;font-size:25px}
.section-heading{position:absolute;left:0;width:1200px;text-align:center;font-family:"Ubuntu",sans-serif;font-weight:400;font-size:30px;line-height:48px;color:var(--ink)}
.section-heading em{font-style:normal;color:var(--orange)}
.value{position:absolute;width:400px;height:90px}
.value .badge{position:absolute;left:0;top:0}
.value h3{position:absolute;left:46px;top:-4px;font-family:"Ubuntu",sans-serif;font-weight:400;font-size:16.5px;color:#333;white-space:nowrap}
.value p{position:absolute;left:46px;top:20px;width:320px;font-size:11.5px;line-height:15px;color:var(--body);text-align:justify}
.btn-apply{position:absolute;left:703px;width:230px;height:54px;border-radius:6px;background:linear-gradient(#4a4a4a,#111 55%,#000);border:2px solid #ddd;box-shadow:0 0 4px rgba(0,0,0,.45);color:var(--gold);font-family:"Ubuntu",sans-serif;font-weight:500;font-size:24px;display:flex;align-items:center;justify-content:center}

/* Footer band */
.footer-band{position:absolute;left:0;top:1905px;width:1200px;height:285px;background:linear-gradient(180deg,var(--orange-band) 0%,var(--orange-band-light) 100%)}
.footer-divider{position:absolute;left:619px;top:0;width:2px;height:285px;background:rgba(200,90,20,.35)}
.feed-name{position:absolute;left:200px;top:28px;display:flex;align-items:center;gap:14px;font-family:"Ubuntu",sans-serif;font-weight:700;font-size:42px;color:var(--white)}
.feed-name i{width:30px;height:30px;border-radius:50%;background:var(--white)}
.tweets{position:absolute;left:200px;top:95px;width:350px;color:var(--white);font-size:13.5px;line-height:18px}
.tweets p{margin-bottom:18px}
.tweets .tag{display:block;color:var(--tweet-link)}
.btn-dark{position:absolute;height:32px;border-radius:4px;background:linear-gradient(#3a3a3a,#000);color:var(--white);font-family:"Ubuntu",sans-serif;font-weight:500;font-size:16px;display:flex;align-items:center;justify-content:center}
.newsletter-title{position:absolute;left:711px;top:42px;font-family:"Ubuntu",sans-serif;font-size:24px;color:var(--white)}
.field{position:absolute;left:712px;width:288px;height:32px;background:var(--white);border:1px solid #e7b48a;border-radius:3px;box-shadow:inset 0 1px 3px rgba(0,0,0,.2);font-style:italic;font-size:11px;color:#888;padding:8px 0 0 15px}

.legal{position:absolute;left:0;top:2190px;width:1200px;height:60px;background:var(--footer);color:#ddd;font-size:10.5px;text-align:right;padding:16px 195px 0 0;line-height:21px}
</style>
</head>
<body>

<header class="site-header">
  <div class="brand">
    <span class="brand-mark"></span>
    <span class="brand-name">Brantley</span>
  </div>
  <nav class="main-nav">
    <a class="is-active" href="#" style="width:95px">Manifeste</a>
    <a href="#" style="width:120px">Opportunités</a>
    <a href="#" style="width:87px">Brantly</a>
    <a href="#" style="width:87px">Postuler</a>
  </nav>
  <div class="social"><span></span><span></span><span></span></div>
</header>

<section class="hero" role="img" aria-label="Photo of colleagues at a desk, one writing in a notebook beside a laptop">
  <div class="hero-arrow" style="left:73px"><svg width="16" height="16" viewBox="0 0 16 16"><path d="M11 2 L5 8 L11 14" fill="none" stroke="#333" stroke-width="3"/></svg></div>
  <div class="hero-arrow" style="left:1065px"><svg width="16" height="16" viewBox="0 0 16 16"><path d="M5 2 L11 8 L5 14" fill="none" stroke="#333" stroke-width="3"/></svg></div>
  <div class="hero-copy">
    <div class="hero-title">Mauris Lacus Vitae Felis Vestibulum Volutpat.</div>
    <p class="hero-text">Cum sociis natoque penatibus et magnis dis parturient montes, nascetur ridiculus mus. In iaculis facilisis massa. Etiam eu urna. Sed porta Cum sociis natoque penatibus et magnis dis parturient montes, nascetur ridiculus mus.</p>
    <div class="btn-more">MORE</div>
  </div>
</section>

<svg width="0" height="0" style="position:absolute">
  <defs>
    <symbol id="badge" viewBox="0 0 40 40">
      <polygon points="6,4 34,4 40,20 34,36 6,36 0,20" fill="#d9d9d9" transform="translate(2,2)"/>
      <polygon points="8,2 30,0 38,18 32,36 6,36 0,18" fill="#f05a22"/>
    </symbol>
  </defs>
</svg>

<!-- Corporate culture -->
<div class="section-rule" style="top:809px"></div>
<div class="ribbon" style="top:790px"><span>Corporate Culture</span></div>
<h2 class="section-heading" style="top:864px">Do You Embrace <em>Brantley's</em><br><em>Corporate Culture?</em></h2>

<div class="value" style="left:162px;top:992px"><svg class="badge" width="40" height="40"><use href="#badge"/><text x="18" y="24" text-anchor="middle" fill="#fff" font-family="Ubuntu,sans-serif" font-size="15">01</text></svg><h3>Eque Ipsa Quae  Inventore Veritatis Et Quasi</h3><p>Sed ut perspiciatis unde omnis iste natus error doloremque laudantium, totam rem aperiam, eaque ipsa quae illo inventore veritatis et quasi architecto beatae vitae</p></div>
<div class="value" style="left:162px;top:1103px"><svg class="badge" width="40" height="40"><use href="#badge"/><text x="18" y="24" text-anchor="middle" fill="#fff" font-family="Ubuntu,sans-serif" font-size="15">02</text></svg><h3>Eque Ipsa Quae  Inventore Veritatis Et Quasi</h3><p>Sed ut perspiciatis unde omnis iste natus error doloremque laudantium, totam rem aperiam, eaque ipsa quae illo inventore veritatis et quasi architecto beatae vitae</p></div>
<div class="value" style="left:162px;top:1214px"><svg class="badge" width="40" height="40"><use href="#badge"/><text x="18" y="24" text-anchor="middle" fill="#fff" font-family="Ubuntu,sans-serif" font-size="15">03</text></svg><h3>Eque Ipsa Quae  Inventore Veritatis Et Quasi</h3><p>Sed ut perspiciatis unde omnis iste natus error doloremque laudantium, totam rem aperiam, eaque ipsa quae illo inventore veritatis et quasi architecto beatae vitae</p></div>
<div class="value" style="left:623px;top:992px"><svg class="badge" width="40" height="40"><use href="#badge"/><text x="18" y="24" text-anchor="middle" fill="#fff" font-family="Ubuntu,sans-serif" font-size="15">04</text></svg><h3>Eque Ipsa Quae  Inventore Veritatis Et Quasi</h3><p>Sed ut perspiciatis unde omnis iste natus error doloremque laudantium, totam rem aperiam, eaque ipsa quae illo inventore veritatis et quasi architecto beatae vitae</p></div>
<div class="value" style="left:623px;top:1103px"><svg class="badge" width="40" height="40"><use href="#badge"/><text x="18" y="24" text-anchor="middle" fill="#fff" font-family="Ubuntu,sans-serif" font-size="15">05</text></svg><h3>Eque Ipsa Quae  Inventore Veritatis Et Quasi</h3><p>Sed ut perspiciatis unde omnis iste natus error doloremque laudantium, totam rem aperiam, eaque ipsa quae illo inventore veritatis et quasi architecto beatae vitae</p></div>
<div class="btn-apply" style="top:1216px">Apply Now</div>

<!-- HR management principles -->
<div class="section-rule" style="top:1390px"></div>
<div class="ribbon" style="top:1371px"><span>HR Management Principles</span></div>
<h2 class="section-heading" style="top:1440px">Do You See Yourself<br><em>Working At Brantley?</em></h2>

<div class="value" style="left:162px;top:1573px"><svg class="badge" width="40" height="40"><use href="#badge"/><text x="18" y="24" text-anchor="middle" fill="#fff" font-family="Ubuntu,sans-serif" font-size="15">01</text></svg><h3>Eque Ipsa Quae  Inventore Veritatis Et Quasi</h3><p>Sed ut perspiciatis unde omnis iste natus error doloremque laudantium, totam rem aperiam, eaque ipsa quae illo inventore veritatis et quasi architecto beatae vitae</p></div>
<div class="value" style="left:162px;top:1684px"><svg class="badge" width="40" height="40"><use href="#badge"/><text x="18" y="24" text-anchor="middle" fill="#fff" font-family="Ubuntu,sans-serif" font-size="15">02</text></svg><h3>Eque Ipsa Quae  Inventore Veritatis Et Quasi</h3><p>Sed ut perspiciatis unde omnis iste natus error doloremque laudantium, totam rem aperiam, eaque ipsa quae illo inventore veritatis et quasi architecto beatae vitae</p></div>
<div class="value" style="left:162px;top:1795px"><svg class="badge" width="40" height="40"><use href="#badge"/><text x="18" y="24" text-anchor="middle" fill="#fff" font-family="Ubuntu,sans-serif" font-size="15">03</text></svg><h3>Eque Ipsa Quae  Inventore Veritatis Et Quasi</h3><p>Sed ut perspiciatis unde omnis iste natus error doloremque laudantium, totam rem aperiam, eaque ipsa quae illo inventore veritatis et quasi architecto beatae vitae</p></div>
<div class="value" style="left:623px;top:1573px"><svg class="badge" width="40" height="40"><use href="#badge"/><text x="18" y="24" text-anchor="middle" fill="#fff" font-family="Ubuntu,sans-serif" font-size="15">04</text></svg><h3>Eque Ipsa Quae  Inventore Veritatis Et Quasi</h3><p>Sed ut perspiciatis unde omnis iste natus error doloremque laudantium, totam rem aperiam, eaque ipsa quae illo inventore veritatis et quasi architecto beatae vitae</p></div>
<div class="value" style="left:623px;top:1684px"><svg class="badge" width="40" height="40"><use href="#badge"/><text x="18" y="24" text-anchor="middle" fill="#fff" font-family="Ubuntu,sans-serif" font-size="15">05</text></svg><h3>Eque Ipsa Quae  Inventore Veritatis Et Quasi</h3><p>Sed ut perspiciatis unde omnis iste natus error doloremque laudantium, totam rem aperiam, eaque ipsa quae illo inventore veritatis et quasi architecto beatae vitae</p></div>
<div class="btn-apply" style="top:1797px">Apply Now</div>

<!-- Footer band -->
<footer class="footer-band">
  <div class="footer-divider"></div>
  <div class="feed-name"><i></i>Chirpwave</div>
  <div class="tweets">
    <p>Velit esse cillum dolore eu fugiat nulla pariatur. Excepteur sint occaecat cupidatat non proident. <span class="tag">@Brantley #EnjeuSanté</span></p>
    <p>Velit esse eu fugiat nulla pariatur. Excepteur sint occaecat cupidatat non proident. <span class="tag">@Brantley #EnjeuSanté</span></p>
  </div>
  <div class="btn-dark" style="left:363px;top:231px;width:141px">More</div>

  <div class="newsletter-title">Newsletter</div>
  <div class="field" style="top:96px">Your Name</div>
  <div class="field" style="top:153px">Your Email</div>
  <div class="btn-dark" style="left:848px;top:212px;width:150px">Abonnez-vous</div>
</footer>

<div class="legal">© 2013 Brantley, All rights reserved<br>X2</div>

</body>
</html>
```